Business Card Re-Design for a Lighting Designer

I would like my business card re-designed. It is currently high gloss and they scratch too easily. I don not think the current design lends itself well to a matte finish. I have included the current design for reference along with our company logo.
Check out our website for current branding.
http://www.brambleorchidstudio.example

Updates
Some of the top contenders are muslim and it is a holiday for them. I do not want to discriminate and would expect the same courtesy for holidays we celebrate.
Target Market(s)
Interior Designers, Architects
Contact Information for Business Card
Logo - Name, Title, Address, Telephone Number and Extension, Email
Font styles to use
Requirements
Must have
- All the information listed on the current business card. If you use Red, it needs to be the red from our logo.
Nice to have
- Vertical and Horizontal Designs will be entertained.
Should not have
- Requirements for a glossy finish...should not look too corporate since we are a design firm.

```html
<!DOCTYPE html>
<html lang="en">
<head>
<meta charset="utf-8">
<title>Bramble Orchid Studio – Business Card</title>
<link rel="stylesheet" href="https://fonts.googleapis.com/css2?family=Roboto:wght@300;400&display=swap">
<style>
  :root {
    --stage: #d6d6d6;
    --card-white: #ffffff;
    --brand-red: #991b1e;
    --ink: #1b1b1b;
    --grey: #8f8f8f;
    --rule: #c98a73;
    --on-red: #ffffff;
  }
  html, body {
    margin: 0;
    padding: 0;
    width: 1200px;
    height: 900px;
    overflow: hidden;
    background: var(--stage);
    font-family: "Roboto", Arial, sans-serif;
  }
  .canvas {
    position: relative;
    width: 1200px;
    height: 900px;
  }
  .card {
    position: absolute;
    top: 83px;
    width: 429px;
    height: 732px;
    box-sizing: border-box;
  }
  .card--front {
    left: 146px;
    background: var(--card-white);
  }
  .card--back {
    left: 635px;
    background: var(--brand-red);
    color: var(--on-red);
    overflow: hidden;
  }

  /* Front: name lockup */
  .brand {
    position: absolute;
    left: 71px;
    top: 182px;
    width: 292px;
  }
  .brand__square {
    width: 64px;
    height: 64px;
    background: var(--brand-red);
    margin-bottom: 36px;
  }
  .brand__name {
    margin: 0;
    font-weight: 300;
    font-size: 46px;
    line-height: 44px;
    letter-spacing: -0.5px;
    color: var(--ink);
    text-transform: uppercase;
  }
  .brand__rule {
    height: 3px;
    background: var(--rule);
    margin: 22px 0 10px;
  }
  .brand__tagline {
    margin: 0;
    font-weight: 400;
    font-size: 17px;
    letter-spacing: 1.3px;
    color: var(--grey);
    text-transform: uppercase;
  }

  /* Back: light pool */
  .light-pool {
    position: absolute;
    left: 40px;
    top: 0;
    width: 350px;
    height: 300px;
    background: radial-gradient(ellipse 50% 62% at 50% 22%,
      rgba(255,255,255,0.95) 0%,
      rgba(240,200,190,0.7) 22%,
      rgba(200,120,110,0.45) 55%,
      rgba(153,27,30,0) 100%);
  }

  .contact {
    position: absolute;
    left: 51px;
    top: 395px;
    text-transform: uppercase;
  }
  .contact__name {
    margin: 0;
    font-weight: 400;
    font-size: 40px;
    line-height: 44px;
    letter-spacing: 0.5px;
  }
  .contact__title {
    margin: 4px 0 0;
    font-weight: 400;
    font-size: 24px;
    letter-spacing: 0.6px;
  }
  .contact__address {
    margin: 32px 0 0;
    font-style: normal;
    font-size: 17px;
    line-height: 29px;
    letter-spacing: 0.6px;
  }
  .contact__lines {
    margin: 26px 0 0;
    padding: 0;
    list-style: none;
    font-size: 16px;
    line-height: 30px;
    letter-spacing: 0.4px;
  }
</style>
</head>
<body>
<main class="canvas">

  <section class="card card--front" aria-label="Card front">
    <div class="brand">
      <div class="brand__square"></div>
      <h1 class="brand__name">Bramble<br>Orchid<br>Studio</h1>
      <div class="brand__rule"></div>
      <p class="brand__tagline">Lighting for Architecture</p>
    </div>
  </section>

  <section class="card card--back" aria-label="Card back">
    <div class="light-pool"></div>
    <div class="contact">
      <h2 class="contact__name">Maren Tollis</h2>
      <p class="contact__title">Principal</p>
      <address class="contact__address">
        512 Larkfield Row Suite 210<br>
        Halden, Oregon 9740 USA
      </address>
      <ul class="contact__lines">
        <li class="contact__phone">55.013.0X7</li>
        <li class="contact__email">maren@brambleorchidstudio.example</li>
        <li class="contact__web">brambleorchidstudio.example</li>
      </ul>
    </div>
  </section>

</main>
</body>
</html>
```